Refinery Service Website (Wholesale) – Luxurious Landing Pages & Industry Hub

We are seeking talented designers to create a luxurious and professional redesign for the wholesale section of our refinery service website, Brightwell VKS. Our current refinery page (https://brightwellvks.example/refinery/) and dental landing page (https://brightwellvks.example/refinery/dental-gold/) provide functional starting points with existing content (words, sections, trust badges, and video placeholders) that must be retained and enhanced with a sophisticated, high-end aesthetic. We serve high-net-worth wholesale clients across industries such as dental practices, mortuaries, estate attorneys, dentists, pawnshops, jewelry stores, and financial advisors. The project includes designing a revamped main wholesale landing page, individual landing pages for each industry with specific sections, and a central hub page to showcase these industries in an SEO-friendly and user-focused way, all while elevating the design to a luxurious standard.

Project Overview
Our refinery service specializes in precious metals and serves a variety of industries through wholesale access. We want the wholesale section of our website to exude sophistication and exclusivity while preserving and enhancing the existing content on our pages. Currently:
• Our refinery page (https://brightwellvks.example/refinery/) provides a basic overview of our services with text, sections, and trust badges, but it lacks visual appeal and a high-end feel.
• Our dental landing page (https://brightwellvks.example/refinery/dental-gold/) targets dental professionals with relevant messaging, sections, and content, but it also feels utilitarian and could benefit from a more elegant design, improved layout, and stronger calls-to-action.
Designers must use the existing words, sections, trust badges, and video placeholders from these pages as a foundation, enhancing them with a luxurious redesign and adding the additional sections specified below. We admire the clean and professional look of https://www.tolvenmetals.example/, but we aim to elevate our design with a more luxurious and exclusive feel to attract discerning wholesale clients. The redesign will involve:
1 Main Wholesale Landing Page: A complete overhaul of our current refinery page into a luxurious and professional entry point, retaining and enhancing existing content while improving the overall design.
2 Industry-Specific Landing Pages: A dedicated landing page for each of the following industries: dental practices, mortuaries, estate attorneys, dentists, pawnshops, jewelry stores, and financial advisors. Each page must retain and enhance existing content (where applicable) and include specific sections (detailed below) to build trust, provide information, and encourage engagement.
3 Industry Hub Page: A central page that showcases all the industries we serve in a visually appealing and SEO-optimized manner, acting as a gateway to each industry-specific landing page.
Our website is built on WordPress using the Bricks Builder, so design submissions should be provided in HTML, CSS, or as a Figma file for seamless integration. The design must be responsive, visually striking, and optimized for usability across all devices (desktop, tablet, mobile).
Project Scope
We are looking for design submissions that include:
• Main Wholesale Landing Page: A redesigned version of our current refinery page (https://brightwellvks.example/refinery/), transformed into a luxurious and professional entry point for our wholesale services. The new design must retain the existing words, sections, trust badges, and any video placeholders, enhancing them with a high-end aesthetic while improving layout and engagement.
• Industry-Specific Landing Pages: A dedicated landing page for each of the following industries: dental practices, mortuaries, estate attorneys, dentists, pawnshops, jewelry stores, and financial advisors. Each page must:
◦ Retain and enhance existing content (words, sections, trust badges, video placeholders) from pages like our dental landing page (https://brightwellvks.example/refinery/dental-gold/) as a reference, adapting it for each industry. For industries without existing pages, mirror the structure and content style of the dental page while tailoring the messaging and visuals.
◦ Include the following additional sections to enhance functionality and trust:
Trust Badges: A section displaying trust signals (e.g., certifications, accreditations, years in business) to build credibility with visitors. Include placeholders for 4–6 badges/icons, enhancing any existing badges from our current pages.
Testimonials: A section featuring 3–5 customer testimonials with placeholders for quotes, names, and industries (e.g., “Dr. Carl Bevin, Dental Practice Owner”). If testimonials exist on current pages, enhance their presentation.
Contact Information: A clearly visible section with contact details (e.g., phone number, email, address) styled to match the luxurious aesthetic, improving any existing contact info presentation.
Contact Fillout Form: A user-friendly form for inquiries, including fields for name, email, industry, and message, with a professional design that encourages submissions, enhancing any existing forms.
Shipping Information: A section detailing shipping instructions and processes (e.g., how to send materials for refining), presented clearly and concisely, building on any existing shipping details.
Summary Service Bullet Points: A concise list of 5–7 key services or benefits tailored to the specific industry (e.g., “Fast turnaround for dental scrap” for dental pages, “Secure handling for jewelry inventory” for jewelers), improving any existing bullet points.
Video: Shipping Instructions: A placeholder for a video explaining how to ship materials to us, styled with a play button and a luxurious frame, enhancing any existing video placeholders.
Video: How Our Refinery Works: A placeholder for a video detailing our refining process, designed to match the aesthetic of the page, enhancing any existing video placeholders.
Video: Who We Are: A placeholder for a video introducing our company and values, presented in an elegant and professional manner, enhancing any existing video placeholders.
◦ Include tailored messaging and design elements that resonate with the specific industry (e.g., dental tools and scrap refining benefits for dental pages, elegant estate visuals for attorneys, jewelry displays for jewelers).
◦ Maintain a cohesive design that ties back to the overall luxurious aesthetic of the wholesale section.
• Industry Hub Page: A central hub page that showcases all the industries we serve in an SEO-friendly and visually engaging way. This page should include:
◦ A grid, carousel, or categorized layout featuring each industry with a concise description or tagline (e.g., “Dental Practices: Turn Scrap into Profit”).
◦ Links to each industry-specific landing page for easy navigation.
◦ Design elements that encourage exploration (e.g., hover effects, icons, or visuals representing each industry).
◦ SEO optimization through keyword-rich headings, meta-friendly layouts, and content areas that naturally incorporate industry terms.
• SEO and User Engagement Focus: The design should balance aesthetics with functionality, ensuring that both the hub page and individual landing pages are optimized for search engines (e.g., through clear headings, meta-friendly layouts) and capture user attention with compelling calls-to-action (e.g., “Discover Refinery Solutions for Your Dental Practice” or “Maximize Value for Your Jewelry Inventory”).
Design Requirements
• Aesthetic: Luxurious, elegant, and professional, with a focus on high-net-worth wholesale clients. The current designs (https://brightwellvks.example/refinery/ and https://brightwellvks.example/refinery/dental-gold/) are too basic and functional; we want a high-end look that conveys prestige and trust, using elements like deep golds, silvers, blacks, or whites to evoke luxury while enhancing existing content.
• Typography: Clean, modern, and sophisticated fonts that enhance readability and align with a high-end brand image, improving upon existing typography.
• Imagery: Incorporate placeholders for high-quality imagery relevant to each industry (e.g., dental tools, jewelry displays, legal documents). No stock images required in submissions—just placeholders. Retain and enhance any existing imagery placeholders from our current pages.
• Video Placeholders: Video sections (for shipping instructions, how the refinery works, and who we are) should include placeholders with play buttons and elegant frames that match the luxurious aesthetic, enhancing any existing video placeholders on our current pages.
• Responsiveness: The design must be fully responsive and look great on desktop, tablet, and mobile devices.
• SEO Optimization: The layout should support SEO best practices, such as clear heading structures (H1, H2, etc.), alt-text-friendly image placeholders, and keyword-rich content areas for each industry, building on existing content for SEO purposes.
• Deliverables Format: Submissions should include design files in HTML, CSS, or Figma format, ready for integration into WordPress with Bricks Builder.

Submission Guidelines
We invite designers to submit their concepts based on the following:
• A mockup of the redesigned main wholesale landing page, improving upon our current refinery page (https://brightwellvks.example/refinery/), retaining and enhancing existing words, sections, trust badges, and video placeholders with a luxurious aesthetic.
• A mockup of the industry hub page showcasing all the industries we serve (dental practices, mortuaries, estate attorneys, dentists, pawnshops, jewelry stores, financial advisors).
• At least two examples of industry-specific landing pages (e.g., one for dental practices, improving upon our current dental page (https://brightwellvks.example/refinery/dental-gold/), and one for jewelry stores), showing how the design retains and enhances existing content, incorporates all required sections (trust badges, testimonials, contact info, contact form, shipping info, service bullet points, and video placeholders), and tailors messaging to each audience.
• A brief explanation of your design choices, including how they enhance SEO, tailor messaging for each industry, incorporate and enhance existing content, include the required sections, and align with the luxurious and professional aesthetic we’re seeking.
• Files in HTML, CSS, or Figma format to demonstrate how the design can be implemented.

Judging Criteria
Submissions will be evaluated based on:
• Alignment with the luxurious and professional aesthetic described, significantly improving upon our current designs (https://brightwellvks.example/refinery/ and https://brightwellvks.example/refinery/dental-gold/) while retaining and enhancing existing content.
• Effective retention and enhancement of existing words, sections, trust badges, and video placeholders from our current pages, seamlessly integrating them into the new design.
• Inclusion and effective design of all required sections (trust badges, testimonials, contact info, contact form, shipping info, service bullet points, and video placeholders) on the industry-specific landing pages.
• Creativity and effectiveness in tailoring messaging and visuals for each industry-specific landing page.
• Usability and visual appeal of the industry hub page, including its potential to improve SEO and engage users.
• Suitability for the target audience (high-net-worth wholesale clients in dental, mortuary, legal, pawnshop, jewelry, and financial sectors).
• Compatibility with WordPress and Bricks Builder (based on the format of deliverables).

Additional Notes
• We are open to creative interpretations of “luxury” and encourage designers to think outside the box while maintaining professionalism. Use our current pages as a foundation for content and structure, enhancing and building upon them rather than replacing them entirely.
• The industry hub page should feel intuitive and encourage exploration, potentially using layouts like a grid, carousel, or categorized sections with hover effects.
• Each industry-specific landing page should include a unique value proposition (e.g., “Streamline Your Dental Scrap Refining Process” or “Maximize Value for Your Jewelry Inventory”) to capture attention, building on the clarity of our current dental page but with a more luxurious presentation and all required sections.
• We will provide feedback during the contest and may request revisions from top submissions.

About Us
Brightwell VKS is a leading refinery service provider specializing in precious metals, offering wholesale solutions to a wide range of industries such as dental, jewelry, and legal sectors. Our goal is to create a luxurious online presence that reflects the high value we provide to our clients.
We look forward to seeing your creative designs and how you can bring our vision of a luxurious, industry-focused wholesale section to life!

```html
<!DOCTYPE html>
<html lang="en">
<head>
<meta charset="utf-8">
<title>Brightwell VKS – Refinery Process</title>
<link href="https://fonts.googleapis.com/css2?family=Montserrat:wght@400;500;600;700;800&family=Open+Sans:wght@400;600&display=swap" rel="stylesheet">
<style>
:root{
  --navy:#1f1c5c;
  --gold:#c9a24a;
  --gold-light:#e6c574;
  --ink:#151515;
  --text:#3a3a3a;
  --muted:#777;
  --line:#d9d9d9;
  --paper:#ffffff;
  --soft:#f4f4f4;
  --footer:#121212;
  --footer-card:#1e1e1e;
}
*{box-sizing:border-box;margin:0;padding:0}
html,body{width:1200px;height:4736px;overflow:hidden}
body{font-family:"Open Sans",Arial,sans-serif;color:var(--text);background:var(--paper);font-size:13px;line-height:1.6}
h1,h2,h3,h4,h5,.nav,.btn{font-family:"Montserrat",Arial,sans-serif}

.ticker{height:24px;border-bottom:1px solid var(--line);display:flex;align-items:center;padding:0 40px;gap:22px;font-size:9px;font-family:"Montserrat",sans-serif;font-weight:600;color:var(--ink)}
.ticker b{color:var(--gold);font-weight:700}
.ticker em{color:#2f9a4a;font-style:normal}

.header{height:44px;display:flex;align-items:center;padding:0 40px;gap:24px}
.brand{display:flex;align-items:center;gap:8px;font-family:"Montserrat",sans-serif;font-weight:700;font-size:14px;color:var(--ink)}
.brand i{width:18px;height:18px;border-radius:50%;background:var(--gold);display:block}
.search{flex:1;height:26px;border:1px solid var(--line);border-radius:13px;display:flex;align-items:center;padding:0 12px;font-size:10px;color:var(--muted)}
.tools{display:flex;gap:12px;align-items:center}
.tools svg{width:18px;height:18px}
.tools .call{width:26px;height:26px;border-radius:50%;background:var(--navy);display:flex;align-items:center;justify-content:center}

.nav{height:40px;background:var(--soft);display:flex;align-items:center;justify-content:space-between;padding:0 60px;font-size:11px;font-weight:600;color:var(--ink)}

.hero{position:relative;height:582px;background:radial-gradient(ellipse 45% 60% at 50% 80%,#f08a2e 0%,#a4481a 25%,#3a2a22 60%,#4a4a4a 100%);overflow:hidden}
.hero h1{position:absolute;left:0;right:0;top:190px;text-align:center;color:#fff;font-size:80px;line-height:1.05;font-weight:800;letter-spacing:2px}
.badges{position:absolute;left:0;right:0;top:470px;display:flex;justify-content:center;gap:16px}
.badge{width:44px;height:44px;border-radius:50%;background:linear-gradient(#2b2b2b,#111);border:3px solid var(--gold)}
.badge.rect{width:96px;border-radius:4px;background:#f1f1f1;border:none}

.about{height:600px;position:relative}
.about .media{position:absolute;left:160px;top:70px;width:320px;height:490px;background:linear-gradient(160deg,#5a5a5a,#2c2c2c 55%,#b8541c);display:flex;align-items:center;justify-content:center}
.play{width:64px;height:64px;border-radius:50%;background:var(--navy);display:flex;align-items:center;justify-content:center}
.about .bar{position:absolute;left:572px;top:76px;width:3px;height:150px;background:var(--ink)}
.about .copy{position:absolute;left:600px;top:70px;width:540px}
.section-title{font-size:28px;font-weight:800;color:var(--ink);line-height:1.15;text-transform:uppercase}
.about .copy h2{margin-bottom:26px;font-size:30px}
.copy p{font-size:12px;margin-bottom:14px}

.features{height:500px;display:flex;gap:12px;padding:12px 16px 0}
.feature{flex:1;display:flex;flex-direction:column}
.feature .img{height:320px}
.f1{background:linear-gradient(150deg,#6b6b6b,#3a3a3a 40%,#c79a2e 75%,#7a5a14)}
.f2{background:linear-gradient(150deg,#8d8d8d,#4a4a4a 50%,#d9d9d9)}
.f3{background:linear-gradient(160deg,#3a2a20,#b84a16 45%,#f3a23a 70%,#2a2a2a)}
.feature h3{margin:-28px 24px 0;background:#fff;padding:16px 10px 8px;text-align:center;font-size:16px;font-weight:800;color:var(--ink);text-transform:uppercase}
.feature p{padding:4px 30px 0;font-size:11.5px;line-height:1.55;text-align:center}

.personal{height:560px;position:relative}
.personal .copy{position:absolute;left:140px;top:40px;width:380px}
.personal h2{font-size:30px;margin-bottom:10px}
.underline{width:60px;height:3px;background:var(--ink);margin-bottom:20px}
.personal .img{position:absolute;left:540px;right:0;top:60px;height:420px;background:linear-gradient(160deg,#e9e9e9,#9a9a9a 35%,#3a3a3a 60%,#d2661f 80%,#5a5a5a)}

.testimonials{height:470px;background:var(--navy);position:relative;padding-top:70px}
.testimonials h2{color:#fff;text-align:center;font-size:28px;margin-bottom:36px}
.cards{display:flex;justify-content:center;gap:26px}
.t-card{width:400px;height:230px;background:#fff;display:flex;gap:20px;padding:28px 24px;position:relative}
.avatar{width:90px;height:90px;background:#3a3a3a;flex:none;margin-top:24px}
.stars{color:var(--gold);font-size:15px;letter-spacing:2px}
.t-card p{font-size:11.5px;margin:6px 0 12px}
.t-card h4{font-size:15px;font-weight:700;color:var(--ink)}
.t-card h4 small{font-family:"Open Sans",sans-serif;font-weight:400;font-size:10px;color:var(--muted);margin-left:6px}
.quote{position:absolute;right:22px;bottom:4px;font-family:Georgia,serif;font-size:60px;line-height:1;color:var(--ink)}
.arrow{position:absolute;top:258px;width:24px;height:24px}
.arrow.l{left:120px}.arrow.r{right:120px}

.register{height:1066px;padding-top:80px}
.register h2{text-align:center;font-size:30px;margin-bottom:44px}
.steps{width:980px;margin:0 auto 56px;display:flex;justify-content:space-between;position:relative}
.steps:before{content:"";position:absolute;left:75px;right:75px;top:65px;height:2px;background:var(--line)}
.step{width:150px;text-align:center;position:relative}
.step .lbl{height:44px;display:flex;align-items:flex-end;justify-content:center;font-family:"Montserrat",sans-serif;font-size:12px;font-weight:600;color:var(--ink);line-height:1.3;margin-bottom:4px}
.step .dot{width:34px;height:34px;margin:0 auto;border-radius:50%;background:#fff;border:2px solid var(--line);display:flex;align-items:center;justify-content:center;font-family:"Montserrat",sans-serif;font-size:11px;font-weight:700;color:var(--muted)}
.step.on .dot{background:var(--navy);border-color:var(--navy);color:#fff}
.form{width:980px;margin:0 auto}
.row{display:flex;gap:22px;margin-bottom:26px}
.field{flex:1}
.field label{display:block;font-size:12px;color:var(--ink);margin-bottom:6px}
.field label b{color:#c23;font-weight:400}
.field .box{height:46px;border:1px solid var(--line)}
.btn{display:block;margin:40px auto 0;width:130px;height:44px;background:var(--navy);color:#fff;border:none;font-size:13px;font-weight:700;letter-spacing:1px}

.footer{height:826px;background:var(--footer);color:#bbb;padding:40px 40px 0}
.promos{display:flex;gap:18px;margin-bottom:32px}
.promo{flex:1;height:100px;border-radius:6px;padding:18px 20px;color:#fff}
.promo h4{font-size:17px;font-weight:700;margin-bottom:6px}
.promo p{font-size:10px}
.promo a{font-size:10px;color:var(--gold-light);text-decoration:underline}
.promo.dark{background:var(--footer-card);border:1px solid #333}
.promo.blue{background:var(--navy)}
.promo.gold{background:linear-gradient(90deg,#5a4618,#b08a36 60%,#e2c06a)}
.promo.gold a{color:#fff}
.cols{display:flex;gap:30px;height:220px}
.col{width:150px;font-size:10px;line-height:1.9}
.col h5{color:#fff;font-size:11px;margin-bottom:4px}
.col a{display:block;color:#bbb;text-decoration:none}
.hours{margin-left:auto;width:240px}
.hours .open{background:var(--footer-card);border:1px solid #333;border-radius:4px;padding:8px 12px;color:#fff;font-size:11px;margin-bottom:12px}
.hours p{font-size:11px;color:#fff}
.flag{width:36px;height:22px;margin-top:8px;background:linear-gradient(#3c3b6e 0 50%,#b22234 50%)}
.news{display:flex;align-items:center;gap:20px;padding:16px 0;border-bottom:1px solid #2c2c2c;font-size:11px;color:#ddd}
.news .in{margin-left:auto;width:240px;height:30px;background:#fff;border-radius:3px;display:flex;align-items:center;justify-content:space-between;padding:0 4px 0 10px;color:var(--muted);font-size:10px}
.news .in span{background:var(--navy);color:#fff;padding:4px 10px;border-radius:2px}
.contact{display:flex;justify-content:space-between;padding:28px 10px;border-bottom:1px solid #2c2c2c;font-family:"Montserrat",sans-serif;font-weight:600;font-size:14px;color:#fff}
.social{display:flex;align-items:center;gap:10px;padding:22px 0;font-size:11px}
.social i{width:18px;height:18px;border-radius:50%;background:#555;display:block}
.copyright{font-size:9px;color:#777;padding-bottom:14px;border-bottom:1px solid #2c2c2c}
.foot-brand{display:flex;align-items:center;gap:12px;padding-top:42px;font-family:"Montserrat",sans-serif;font-weight:600;font-size:22px;color:#fff;letter-spacing:1px}
.foot-brand i{width:30px;height:30px;border-radius:50%;background:var(--gold);display:block}
</style>
</head>
<body>

<div class="ticker">
  <span>GOLD <b>$2,341.20</b> <em>+4.10</em></span>
  <span>SILVER <b>$29.84</b> <em>+0.22</em></span>
  <span>PLATINUM <b>$998.50</b> <em>+2.30</em></span>
  <span>PALLADIUM <b>$972.40</b> <em>+1.80</em></span>
</div>

<header class="header">
  <div class="brand"><i></i>Brightwell VKS Refineries</div>
  <div class="search">Search products and services...</div>
  <div class="tools">
    <svg viewBox="0 0 24 24" fill="none" stroke="#151515" stroke-width="2"><circle cx="12" cy="8" r="4"/><path d="M4 21c1-5 15-5 16 0"/></svg>
    <svg viewBox="0 0 24 24" fill="none" stroke="#151515" stroke-width="2"><path d="M3 4h3l2 11h11l2-8H7"/><circle cx="9" cy="20" r="1.5"/><circle cx="18" cy="20" r="1.5"/></svg>
    <span class="call"><svg viewBox="0 0 24 24" width="12" height="12" fill="#fff"><path d="M6 2l4 4-2 3c1 2 3 4 5 5l3-2 4 4-3 4C10 20 4 14 2 5z"/></svg></span>
  </div>
</header>

<nav class="nav"><span>Gold</span><span>Silver</span><span>Shop All</span><span>Deals</span><span>Sell to us</span><span>We Buy</span><span>IRA</span><span>Jewelry</span></nav>

<section class="hero" role="img" aria-label="Refinery worker pouring molten gold from a crucible">
  <h1>REFINERY<br>PROCESS</h1>
  <div class="badges"><div class="badge"></div><div class="badge"></div><div class="badge"></div><div class="badge"></div><div class="badge rect"></div></div>
</section>

<section class="about">
  <div class="media" role="img" aria-label="Video: molten metal being poured inside the refinery">
    <span class="play"><svg width="22" height="22" viewBox="0 0 24 24"><path d="M7 4l14 8-14 8z" fill="#fff"/></svg></span>
  </div>
  <div class="bar"></div>
  <div class="copy">
    <h2 class="section-title">About our precious<br>metal refinery</h2>
    <p>Most refineries are set up to work on precious metals behind closed doors. Here at Brightwell VKS we not only invite you to witness your lot being melted, we encourage you to watch every step of your metals being processed. We have a comfortable seating area with bulletproof walls and windows for you to witness the melting as it is taking place.</p>
    <p>Our precious metal refinery is equipped with the latest technology and state of the art assaying equipment used to find each lot of your precious metals, ensuring your results are both accurate and precise. You will receive an analysis of your metals, itemizing the results and giving you peace of mind.</p>
    <p>We take pride in our timeliness and efficiency. We know that time is money and your time is valuable, so we will give you your lots settlement in a matter of hours, with your choice of cash, check or wire transfer. Please call ahead and schedule a same-day appointment at our facility.</p>
  </div>
</section>

<section class="features">
  <article class="feature">
    <div class="img f1" role="img" aria-label="Gold grain pieces in a refining tray"></div>
    <h3>Optimize your earnings</h3>
    <p>You are able to receive the most cash for your silver through us. Why? Because we are the refinery! This allows us to give you the most money. No need to go through cash for gold places or pawn shops, our in-house refinery gives you direct access to those savings.</p>
  </article>
  <article class="feature">
    <div class="img f2" role="img" aria-label="Refinery worker handling precious metal scrap"></div>
    <h3>No middle-man</h3>
    <p>At Brightwell VKS we melt gold and silver received from buying gold and authorized dealers such as pawn shops and we buy gold pieces. Doesn't it make sense to cut them out? Deal direct with us, we're confident you'll walk out happy!</p>
  </article>
  <article class="feature">
    <div class="img f3" role="img" aria-label="Molten gold poured from a glowing crucible"></div>
    <h3>Trust &amp; reputation</h3>
    <p>Dealing direct also gives you access to our resources: industry standard technology allowing us to treat your items with the utmost care. Our process is clear as we will protect the integrity of your jewelry through our non-invasive process whether or not you decide to sell.</p>
  </article>
</section>

<section class="personal">
  <div class="copy">
    <h2 class="section-title">Personal<br>relationships</h2>
    <div class="underline"></div>
    <p>We at Brightwell VKS Refineries recognize the value of personal relationships and the details that take service from good to great. We strive to build a personal relationship with our clients. By gaining your confidence and giving consistent accurate results, we work diligently to earn your trust. Ensuring our client's complete satisfaction is our number one goal.</p>
    <p>Brightwell VKS Refineries is built on the idea that trust is the most important asset to a successful business. We strive to earn your trust and confidence every day through transparency, accuracy and personal relationships with each and every client. We recognize that trust is valuable and we at Brightwell VKS want to earn yours.</p>
    <p>Trust can only be earned, give us the opportunity to serve you.</p>
  </div>
  <div class="img" role="img" aria-label="Worker in protective gear pouring molten metal"></div>
</section>

<section class="testimonials">
  <h2 class="section-title">What our clients say</h2>
  <svg class="arrow l" viewBox="0 0 24 24" fill="none" stroke="#fff" stroke-width="2.5"><path d="M15 4l-8 8 8 8"/></svg>
  <svg class="arrow r" viewBox="0 0 24 24" fill="none" stroke="#fff" stroke-width="2.5"><path d="M9 4l8 8-8 8"/></svg>
  <div class="cards">
    <div class="t-card">
      <div class="avatar" role="img" aria-label="Client portrait placeholder"></div>
      <div>
        <div class="stars">★★★★★</div>
        <p>Lorem ipsum dolor sit amet, consectetur adipiscing elit, sed do eiusmod tempor incididunt ut labore et dolore magna aliqua. Ut enim ad minim veniam, quis nostrud exercitation ullamco.</p>
        <h4>John Doe<small>Company name</small></h4>
      </div>
      <span class="quote">&rdquo;</span>
    </div>
    <div class="t-card">
      <div class="avatar" role="img" aria-label="Client portrait placeholder"></div>
      <div>
        <div class="stars">★★★★★</div>
        <p>Lorem ipsum dolor sit amet, consectetur adipiscing elit, sed do eiusmod tempor incididunt ut labore et dolore magna aliqua. Ut enim ad minim veniam, quis nostrud exercitation ullamco.</p>
        <h4>John Doe<small>Company name</small></h4>
      </div>
      <span class="quote">&rdquo;</span>
    </div>
  </div>
</section>

<section class="register">
  <h2 class="section-title">Wholesale registration</h2>
  <div class="steps">
    <div class="step on"><div class="lbl">Business Contact<br>Information</div><div class="dot">01</div></div>
    <div class="step on"><div class="lbl">Primary Owner<br>or Principal</div><div class="dot">02</div></div>
    <div class="step"><div class="lbl">Secondary Owner<br>or Principal</div><div class="dot">03</div></div>
    <div class="step"><div class="lbl">Billing</div><div class="dot">04</div></div>
    <div class="step"><div class="lbl">Shipping</div><div class="dot">05</div></div>
  </div>
  <div class="form">
    <div class="row">
      <div class="field"><label>First name<b>*</b></label><div class="box"></div></div>
      <div class="field"><label>Last name<b>*</b></label><div class="box"></div></div>
      <div class="field"><label>Position<b>*</b></label><div class="box"></div></div>
    </div>
    <div class="row">
      <div class="field"><label>Phone<b>*</b></label><div class="box"></div></div>
      <div class="field"><label>Email<b>*</b></label><div class="box"></div></div>
    </div>
    <div class="row">
      <div class="field"><label>Address Line 1<b>*</b></label><div class="box"></div></div>
      <div class="field"><label>Address Line 2<b>*</b></label><div class="box"></div></div>
      <div class="field"><label>City<b>*</b></label><div class="box"></div></div>
    </div>
    <div class="row">
      <div class="field"><label>State<b>*</b></label><div class="box"></div></div>
      <div class="field"><label>Postal / Zip Code<b>*</b></label><div class="box"></div></div>
    </div>
    <button class="btn">NEXT</button>
  </div>
</section>

<footer class="footer">
  <div class="promos">
    <div class="promo dark"><h4>Price match guarantee</h4><p>on all bullion products</p><a>Learn more</a></div>
    <div class="promo blue"><h4>100% Insured</h4><p>All orders are tracked and insured.</p></div>
    <div class="promo gold"><h4>Free Shipping</h4><p>Orders ship free over $199</p><a>Learn more</a></div>
  </div>
  <div class="cols">
    <div class="col"><h5>Buying &amp; selling</h5><a>Shop Bullion</a><a>Bar Bullion</a><a>Silver Bullion</a><a>Gold Bullion</a><a>Platinum Bullion</a><a>Palladium Bullion</a><a>Refinery Services</a></div>
    <div class="col"><h5>Company</h5><a>Leave a Review</a><a>Testimonials</a><a>Wellness Process</a><a>Blog</a><a>About Us</a></div>
    <div class="col"><h5>Customer care</h5><a>My Account</a><a>Investment Tools</a><a>Contact us</a><a>FAQs</a><a>Jewelry 360</a><a>Jewelry Repair</a></div>
    <div class="col"><h5>Legal</h5><a>Privacy Policy</a><a>Terms and Conditions</a><a>Mail-In Terms</a><a>Acceptable Use</a><a>Cookie Policy</a><a>Disclaimer Policy</a><a>Payment Terms</a><a>Shipping Policy</a></div>
    <div class="hours">
      <div class="open">Open Mon-Fri<br><b>10:00a - 5:00p PST</b></div>
      <p>Brightwell VKS Refineries is a proudly patriotic Christian business in the United States of America.</p>
      <div class="flag" role="img" aria-label="National flag"></div>
    </div>
  </div>
  <div class="news">Subscribe to our newsletter to be the first to know about special deals and promotions.<div class="in">Enter Email<span>Go</span></div></div>
  <div class="contact"><span>(555) 014-2290</span><span>420 Alder Ridge Rd, Linwood, OR 97000</span><span>info@brightwellvks.example</span></div>
  <div class="social">Follow us on our social media to stay up to date. <i></i><i></i><i></i><i></i><i></i></div>
  <div class="copyright">© 2025 Brightwell VKS Refineries. All rights reserved.</div>
  <div class="foot-brand"><i></i>Brightwell VKS Refineries</div>
</footer>

</body>
</html>
```